Patent Law

Need to develop a home page for a patent lawyer.

Colors should go with logo, blues...

Company Name- Corvel Tindry, PLLC

Company Overview-

I am an Intellectual Property Lawyer and focus on patents, copyrights, trademarks, & trade secrets. I work with small businesses and start ups in the chemical and biotech industries.

Why Us-

I am small firm that can provide large-firm service at a reasonable price. I also can charge flat-fees for entreprenuers in certain practice areas.

Services-
Intellectual Property
Patents
Copyrights
Trademarks
Trade secrets
Healthcare Compliance
Elder law
Wills
Trusts

Website we like-
http://www.quarnlowtide.example/ - within industry!!
http://www.vopperhask.example/
http://dulbrickovan.example/
http://thefernwoldguides.example/

Target Market(s)

My customers will be small business, specifically small start-up companies in the chemical and biotech arena.

Industry/Entity Type

Trade

Requirements
Must have
• Colors should go with logo, blues...

```html
<!DOCTYPE html>
<html lang="en">
<head>
<meta charset="utf-8">
<title>Corvel Tindry, PLLC — Intellectual Property Law</title>
<link rel="stylesheet" href="https://fonts.googleapis.com/css2?family=Arimo:wght@400;700&family=PT+Sans:wght@700&display=swap">
<style>
:root{
  --page:#efefef;
  --topline:#595959;
  --blue:#1e86d9;
  --blue-dark:#1262b5;
  --blue-text:#1d8be0;
  --ink:#5a5a5a;
  --muted:#8a8a8a;
  --footer-top:#5a5a5a;
  --footer-bottom:#353535;
  --footer-text:#e6e6e6;
  --footer-line:#6c6c6c;
  --base:#3b3b3b;
}
*{margin:0;padding:0;box-sizing:border-box}
html,body{width:803px;height:1200px;overflow:hidden}
body{position:relative;background:var(--page);font-family:"Arimo",Arial,sans-serif;color:var(--ink)}
.abs{position:absolute}
.top-line{left:0;top:0;width:803px;height:6px;background:var(--topline)}

.brand{left:55px;top:80px;display:flex;align-items:center;gap:7px}
.brand-dot{width:12px;height:12px;border-radius:50%;background:var(--blue-dark)}
.brand-name{font-size:11px;color:#2b3550;letter-spacing:.5px;text-transform:uppercase}

.social{display:flex;gap:6px}
.social span{width:18px;height:18px;border-radius:3px;background:var(--blue)}
.header-social{left:651px;top:37px}
.call{left:641px;top:65px}
.call-label{position:absolute;left:27px;top:1px;font-size:9.5px;letter-spacing:.8px;color:#666;white-space:nowrap}
.call-number{position:absolute;left:28px;top:12px;font-size:9.5px;letter-spacing:.6px;color:var(--blue-text);white-space:nowrap}

.nav{left:0;top:107px;width:803px;height:30px;background:linear-gradient(#3196dc,#1670bb);border-bottom:1px solid #0f5a99}
.nav a{position:absolute;top:8px;font-size:11px;letter-spacing:1px;color:#fff;text-decoration:none}
.nav .current{left:45px;top:6px;width:47px;height:18px;background:#5aa9e4;border-radius:2px;text-align:center;padding-top:2px}
.search{left:632px;top:6px;width:129px;height:18px;display:flex}
.search-field{width:88px;background:#fff;font-size:10px;color:#aaa;padding:3px 8px;letter-spacing:.5px}
.search-button{width:41px;background:linear-gradient(#9a9a9a,#6f6f6f);display:flex;align-items:center;justify-content:center}

.hero{left:33px;top:153px;width:509px;height:326px;background:linear-gradient(170deg,#6a6d75 0%,#3a3b42 35%,#1d1e24 70%,#131318 100%)}
.hero-title{left:28px;top:180px;font-family:"PT Sans",Arial,sans-serif;font-size:22px;letter-spacing:1.5px;color:#fff}
.hero-copy{left:28px;top:210px;width:262px;font-size:9.5px;line-height:11px;letter-spacing:.75px;color:#fff}
.dots{left:31px;top:283px;display:flex;gap:5px}
.dots span{width:11px;height:11px;border-radius:50%;background:var(--blue)}
.dots span:first-child{background:#fff}

.welcome{left:542px;top:153px;width:224px;height:326px;background:linear-gradient(#2b8ae0,#1258c0)}
.welcome-notch{left:-14px;top:30px}
.welcome-kicker{top:38px;width:100%;text-align:center;font-size:9.5px;font-weight:700;letter-spacing:1px;color:#fff}
.welcome-name{top:50px;width:100%;text-align:center;font-size:13px;font-weight:700;letter-spacing:1.3px;color:#fff}
.welcome-copy{left:21px;top:80px;width:187px;font-size:9.5px;line-height:11.7px;letter-spacing:.75px;color:#fff;text-align:justify}
.welcome-copy p+p{margin-top:12px}

.services{left:35px;top:509px;width:736px;height:319px;border:1px solid #dcdcdc;border-radius:5px;background:linear-gradient(#f9f9f9,#e4e4e4);box-shadow:0 8px 10px -8px rgba(0,0,0,.25)}
.services-tab{left:341px;top:494px;width:125px;height:29px;border-radius:4px;background:linear-gradient(#3a9ce6,#1a73c9);color:#fff;font-size:15px;letter-spacing:.8px;text-align:center;line-height:29px}
.slider-arrow{top:577px;width:24px;height:102px;border-radius:3px;background:linear-gradient(#3595e0,#146bc4);display:flex;align-items:center;justify-content:center}
.slider-arrow.prev{left:27px}
.slider-arrow.next{left:755px}

.service{top:555px;width:212px}
.service-photo{position:relative;height:146px;border-top:6px solid var(--blue)}
.service-photo::after{content:"";position:absolute;left:106px;top:-1px;border:5px solid transparent;border-top-color:var(--blue)}
.photo-copyright{background:linear-gradient(135deg,#9fd0f3,#3a7fc3 55%,#1c3f78)}
.photo-health{background:linear-gradient(135deg,#c9ccd2,#727883 50%,#2c2f36)}
.photo-ideas{background:linear-gradient(135deg,#3a4a58,#1e3046 50%,#0f1a28)}
.service-title{margin-top:11px;font-size:10px;font-weight:700;letter-spacing:1px;color:var(--blue-text)}
.service-copy{margin-top:7px;font-size:9.5px;line-height:12px;letter-spacing:.4px;color:var(--muted);text-align:justify;height:47px}
.service-more{position:relative;margin-top:4px;height:19px}
.service-more::before{content:"";position:absolute;left:0;right:-4px;top:9px;border-top:1px solid #bdbdbd}
.read-more{position:absolute;left:73px;top:0;width:58px;height:19px;border-radius:3px;background:linear-gradient(#3a9ce6,#1a73c9);color:#fff;font-size:9.5px;text-align:center;line-height:19px;letter-spacing:.3px}

.footer{left:0;top:882px;width:803px;height:286px;background:linear-gradient(var(--footer-top),var(--footer-bottom));color:var(--footer-text)}
.footer h2{position:absolute;top:21px;font-size:13px;font-weight:400;letter-spacing:1.3px}
.rule{position:absolute;height:1px;background:var(--footer-line)}
.news{left:63px;width:266px;height:68px}
.news-thumb{position:absolute;left:0;top:0;width:97px;height:68px;background:#1b1b1b;padding:4px}
.news-thumb div{width:100%;height:100%;background:linear-gradient(135deg,#f3f3f3,#cfd4d8 60%,#7d7f82)}
.news-title{position:absolute;left:104px;top:4px;font-size:10.5px;font-weight:700;letter-spacing:.5px;color:#fff;white-space:nowrap}
.news-copy{position:absolute;left:104px;top:19px;width:160px;font-size:9px;line-height:11.5px;letter-spacing:.5px;color:#cfcfcf}
.news-copy span{color:var(--blue-text)}
.view-all{left:69px;top:243px;font-size:9px;letter-spacing:.8px}
.quicklinks{left:388px;top:68px;list-style:none;font-size:11px;letter-spacing:.6px}
.quicklinks li{height:22.7px}
.quicklinks li::before{content:"›";margin-right:6px}
.location-line{left:610px;font-size:10.5px;line-height:12.3px;letter-spacing:.7px}
.icon{left:590px}
.footer-social{left:609px;top:186px}
.base{left:0;top:1168px;width:803px;height:32px;background:var(--base);font-size:9px;letter-spacing:.6px;color:#d8d8d8}
.base-left{left:62px;top:8px}
.base-right{left:586px;top:8px;white-space:nowrap}
.base-right .sep{margin:0 10px}
</style>
</head>
<body>
<div class="abs top-line"></div>

<header>
  <div class="abs brand"><span class="brand-dot"></span><span class="brand-name">Corvel Tindry, PLLC</span></div>
  <div class="abs social header-social" aria-label="Social links"><span></span><span></span><span></span><span></span></div>
  <div class="abs call">
    <svg width="16" height="18" viewBox="0 0 16 18"><path d="M4 1 L7 5 L5 7 Q6 11 10 13 L12 11 L15 14 L12 17 Q2 14 1 4 Z" fill="#1d8be0"/></svg>
    <span class="call-label">CALL US TODAY</span>
    <span class="call-number">(02)-1234-12345</span>
  </div>
</header>

<nav class="abs nav">
  <a class="current" href="#">HOME</a>
  <a href="#" style="left:122px">ABOUT US</a>
  <a href="#" style="left:217px">SERVICES</a>
  <a href="#" style="left:315px">LATEST NEWS</a>
  <a href="#" style="left:436px">CONTACT US</a>
  <div class="abs search">
    <div class="search-field">Search</div>
    <div class="search-button"><svg width="14" height="10" viewBox="0 0 14 10"><circle cx="5" cy="4.5" r="3.3" fill="none" stroke="#222" stroke-width="1.6"/><line x1="7.5" y1="6.5" x2="12.5" y2="9" stroke="#222" stroke-width="2"/></svg></div>
  </div>
</nav>

<section class="abs hero" role="img" aria-label="Photo of a crowd of black umbrellas with a single red umbrella standing out">
  <h1 class="abs hero-title">HEADLINE TEXT HERE</h1>
  <p class="abs hero-copy">Lorem ipsum dolor sit amet, consectetur adipiscing elit. Curabitur lacinia pretium risus ac euismod. Jurabitur lacinia pretium risus ac euismod.</p>
  <div class="abs dots"><span></span><span></span><span></span></div>
</section>

<aside class="abs welcome">
  <svg class="abs welcome-notch" width="15" height="24" viewBox="0 0 15 24"><path d="M15 0 L0 12 L15 24 Z" fill="#2a88df"/></svg>
  <div class="abs welcome-kicker">WELCOME TO</div>
  <div class="abs welcome-name">CORVEL TINDRY</div>
  <div class="abs welcome-copy">
    <p>I am an Intellectual Property Lawyer and focus on patents, copyrights, trademarks, &amp; trade secrets. I work with small businesses and start ups in the chemical and biotech industries.</p>
    <p>Etiam ante dolor, malesuada nec lobortis sit amet, rutrum malesuada risus. Aliquam tristique velit non eros tincidunt, non dignissim ante gravida. Integer purus eros.</p>
  </div>
</aside>

<section class="abs services"></section>
<div class="abs services-tab">Our Services</div>
<div class="abs slider-arrow prev"><svg width="10" height="44" viewBox="0 0 10 44"><path d="M8 2 L2 22 L8 42" fill="none" stroke="#fff" stroke-width="1.5"/></svg></div>
<div class="abs slider-arrow next"><svg width="10" height="44" viewBox="0 0 10 44"><path d="M2 2 L8 22 L2 42" fill="none" stroke="#fff" stroke-width="1.5"/></svg></div>

<article class="abs service" style="left:63px">
  <div class="service-photo photo-copyright" role="img" aria-label="Photo of a copyright symbol on a glowing digital screen"></div>
  <h3 class="service-title">COPYRIGHT SERVICE</h3>
  <p class="service-copy">Lorem ipsum dolor sit amet, consectetur adipiscing elit. Curabitur lacinia pretium risus ac euismod.</p>
  <div class="service-more"><span class="read-more">read more</span></div>
</article>
<article class="abs service" style="left:295px">
  <div class="service-photo photo-health" role="img" aria-label="Photo of a stethoscope resting on a computer keyboard"></div>
  <h3 class="service-title">HEALTHCARE COMPLIANCE</h3>
  <p class="service-copy">Lorem ipsum dolor sit amet, consectetur adipiscing elit. Curabitur lacinia pretium risus ac euismod.</p>
  <div class="service-more"><span class="read-more">read more</span></div>
</article>
<article class="abs service" style="left:528px">
  <div class="service-photo photo-ideas" role="img" aria-label="Photo of one lit light bulb in a row of unlit bulbs"></div>
  <h3 class="service-title">INTELLECTUAL PROPERTY</h3>
  <p class="service-copy">Lorem ipsum dolor sit amet, consectetur adipiscing elit. Curabitur lacinia.</p>
  <div class="service-more"><span class="read-more">read more</span></div>
</article>

<footer class="abs footer">
  <h2 style="left:62px">LATEST NEWS</h2>
  <h2 style="left:377px">QUICKLINKS</h2>
  <h2 style="left:586px">LOCATION</h2>
  <div class="rule" style="left:62px;top:55px;width:268px"></div>
  <div class="rule" style="left:373px;top:55px;width:156px"></div>
  <div class="rule" style="left:586px;top:55px;width:155px"></div>

  <div class="abs news" style="top:70px">
    <div class="news-thumb" role="img" aria-label="Photo of a presenter pointing at a chart during a meeting"><div></div></div>
    <div class="news-title">News title goes here here.</div>
    <p class="news-copy">Lorem ipsum dolor sit amet, consectetur adipiscing elit...<br><span>more &gt;&gt;</span></p>
  </div>
  <div class="rule" style="left:62px;top:146px;width:268px"></div>
  <div class="abs news" style="top:154px">
    <div class="news-thumb" role="img" aria-label="Photo of a presenter pointing at a chart during a meeting"><div></div></div>
    <div class="news-title">News title goes here here.</div>
    <p class="news-copy">Lorem ipsum dolor sit amet, consectetur adipiscing elit...<br><span>more &gt;&gt;</span></p>
  </div>
  <div class="rule" style="left:62px;top:232px;width:268px"></div>
  <div class="abs view-all">VIEW ALL NEWS</div>

  <ul class="abs quicklinks">
    <li>Home</li><li>About us</li><li>Services</li><li>Latest News</li><li>Contact us</li>
  </ul>
  <div class="rule" style="left:373px;top:232px;width:156px"></div>

  <svg class="abs icon" style="top:70px" width="13" height="12" viewBox="0 0 13 12"><path d="M6.5 0 L13 6 L11 6 L11 12 L2 12 L2 6 L0 6 Z" fill="#e6e6e6"/></svg>
  <div class="abs location-line" style="top:69px">1344 Your Address<br>Location here, NY<br>Country name</div>
  <svg class="abs icon" style="top:117px;left:592px" width="11" height="12" viewBox="0 0 16 18"><path d="M4 1 L7 5 L5 7 Q6 11 10 13 L12 11 L15 14 L12 17 Q2 14 1 4 Z" fill="#e6e6e6"/></svg>
  <div class="abs location-line" style="top:117px">(02)-1234-5678<br>(02)-1234-5679</div>
  <svg class="abs icon" style="top:155px;left:591px" width="14" height="10" viewBox="0 0 14 10"><rect width="14" height="10" fill="#e6e6e6"/><path d="M0 0 L7 6 L14 0" fill="none" stroke="#555" stroke-width="1.2"/></svg>
  <div class="abs location-line" style="top:154px">your@email.com</div>
  <div class="abs social footer-social" aria-label="Social links"><span></span><span></span><span></span><span></span></div>
  <div class="rule" style="left:586px;top:232px;width:155px"></div>
</footer>

<div class="abs base">
  <span class="abs base-left">Copyright 2013 · All rights reserved</span>
  <span class="abs base-right">Sitemap<span class="sep">|</span>FAQ<span class="sep">|</span>Privacy Policy</span>
</div>
</body>
</html>
```